Outdoor Billboard on PVC (double sides)

Hello, i need special design for billboard which is located 15 meters away from the main road. Measures form Billboard: 8 meters X 2 meters. I need Billboard for Window tinting. I have one picture (white Brevanti) which you can use as a main BIG Picture- or you have better idea i am so open to your suggestions. Billboard has to be shocking ... i want to make it look like this is similiar way from style. I have a lot of pictures from my cars which i have done in my garage which we can use it. I dont know if you can use this ... quality? On the billboard so it blames be turn left in 30Meter. My logo wants bi attached- please use it on black background. text which schould be down on the Billboard: Proffesionale Tint my logo VELUNAR put somewhere where looks cool Phone: 0681 2495 307 E-mail: marlow.velunar@kestramail.com Website: www. velunar-glasdunkel.at

Target Market(s)

This billboard wants to be on the border between two countrys..i have my garage company here on the border- where ia am making window. A lot of cars are driving each day nearby so I want that people see this and so they look at where they have left to my garage.

Colors

Designer to choose colors to be used in the design.

Requirements
Must have
• Billboard schould have a BiG picture from white Brevanti with my logo on the side and text Proffesional scarf tint. Down on the board it schould be info Tel, email, website. This measures 8x2 meters

```html
<!DOCTYPE html>
<html lang="de">
<head>
<meta charset="utf-8">
<title>VELUNAR – Billboard</title>
<link rel="stylesheet" href="https://fonts.googleapis.com/css2?family=Bebas+Neue&family=Open+Sans:wght@700&display=swap">
<style>
  :root {
    --page-bg: #e9ecef;
    --board-black: #060606;
    --stripe-brown: #3a2420;
    --accent-red: #e3232a;
    --text-white: #ffffff;
    --car-light: #e4e5e7;
    --car-mid: #b9bcc0;
    --car-dark: #2b2c2e;
  }
  * { margin: 0; padding: 0; box-sizing: border-box; }
  html, body { width: 1200px; height: 840px; overflow: hidden; }
  body { background: var(--page-bg); position: relative; }

  .billboard {
    position: absolute;
    left: 30px; top: 231px;
    width: 1140px; height: 378px;
    background: var(--board-black);
    overflow: hidden;
  }
  .billboard__stripes { position: absolute; inset: 0; }

  .headline {
    position: absolute;
    left: 54px; top: 52px;
    font-family: "Bebas Neue", "Oswald", sans-serif;
    font-size: 60px;
    letter-spacing: 2.5px;
    line-height: 1;
    color: var(--text-white);
    white-space: nowrap;
  }
  .headline__accent { color: var(--accent-red); }

  .hero-car {
    position: absolute;
    left: 20px; top: 168px;
    width: 650px; height: 210px;
    border-radius: 120px 150px 0 0 / 70px 90px 0 0;
    background: linear-gradient(180deg, var(--car-light) 0%, var(--car-mid) 70%, var(--car-dark) 100%);
  }

  .brand {
    position: absolute;
    left: 790px; top: 118px;
    width: 320px;
    display: flex; flex-direction: column; align-items: center;
  }
  .brand__name {
    font-family: "Bebas Neue", "Oswald", sans-serif;
    font-size: 76px;
    letter-spacing: 2px;
    line-height: 1;
    color: var(--accent-red);
  }
  .brand__phone {
    margin-top: 20px;
    background: var(--accent-red);
    color: var(--text-white);
    font-family: "Bebas Neue", "Oswald", sans-serif;
    font-size: 40px;
    letter-spacing: 1.5px;
    line-height: 1;
    padding: 8px 22px 5px;
    border-radius: 16px;
  }

  .contact {
    position: absolute;
    left: 806px; top: 288px;
    list-style: none;
    font-family: "Open Sans", Arial, sans-serif;
    font-weight: 700;
    font-size: 14px;
    color: var(--text-white);
  }
  .contact__item { display: flex; align-items: center; gap: 8px; margin-bottom: 7px; white-space: nowrap; }
  .contact__icon { width: 14px; height: 14px; flex: none; }
</style>
</head>
<body>
  <section class="billboard">
    <svg class="billboard__stripes" width="1140" height="378" viewBox="0 0 1140 378" aria-hidden="true">
      <polygon points="85,0 310,0 0,300 0,85" fill="var(--stripe-brown)"/>
      <polygon points="350,0 480,0 180,378 60,378" fill="var(--stripe-brown)"/>
    </svg>

    <h1 class="headline">Proffesionelle <span class="headline__accent">Sceibentönung</span></h1>

    <div class="hero-car" role="img" aria-label="Weißer Brevanti Sportwagen in Seitenansicht mit getönten Scheiben"></div>

    <div class="brand">
      <span class="brand__name">VELUNAR</span>
      <span class="brand__phone">0681 2495 307</span>
    </div>

    <ul class="contact">
      <li class="contact__item">
        <svg class="contact__icon" viewBox="0 0 14 14" aria-hidden="true"><rect x="1" y="3" width="12" height="8" fill="#fff"/><polyline points="1,3 7,8 13,3" fill="none" stroke="#060606" stroke-width="1.4"/></svg>
        marlow.velunar@kestramail.com
      </li>
      <li class="contact__item">
        <svg class="contact__icon" viewBox="0 0 14 14" aria-hidden="true"><circle cx="7" cy="7" r="6" fill="none" stroke="#fff" stroke-width="1.4"/><ellipse cx="7" cy="7" rx="2.6" ry="6" fill="none" stroke="#fff" stroke-width="1.2"/><line x1="1" y1="7" x2="13" y2="7" stroke="#fff" stroke-width="1.2"/></svg>
        www.velunar-glasdunkel.at
      </li>
    </ul>
  </section>
</body>
</html>
```